Web Redesign of Investment Management Solution Provider

Redesign of existing website. Need a very elegant and professional look. (See attached file for details)
Only PSD files wanted. No HTML.
Looking for a long term association with able designers who would be able to work further on application design. Winner in this contest would get brownie points in the next 'large contract' that I launch for a web app design.
Updates
Only PSD outputs wanted. HTMLs not required. We would post that as a separate project once we get the designs.
Payment changed to guaranteed.
Target Market(s)
Fund managers, hedge funds, wealth managers
Industry/Entity Type
Investment
Look and feel

```html
<!DOCTYPE html>
<html lang="en">
<head>
<meta charset="utf-8">
<title>Fundora — Investment Management Solutions</title>
<link href="https://fonts.googleapis.com/css2?family=Arimo:ital,wght@0,400;0,700;1,400&display=swap" rel="stylesheet">
<style>
:root{
  --teal:#2a9cbd;
  --teal-light:#6cc7e0;
  --orange:#e8752a;
  --orange-light:#f9b233;
  --text:#444;
  --heading:#e06a2c;
  --link-blue:#2b8fb8;
  --footer:#7a7a7a;
  --nav-top:#e9e9e9;
  --nav-bottom:#a9a9a9;
  --panel:#fff;
}
*{box-sizing:border-box;margin:0;padding:0}
html,body{width:1200px;height:938px;overflow:hidden;background:#fff;font-family:"Arimo",Arial,sans-serif;color:var(--text)}
.page{position:relative;width:1200px;height:938px;overflow:hidden}

.hero{position:absolute;left:0;top:0;width:1200px;height:508px}
.hero-scene{position:absolute;inset:0;
  background:linear-gradient(180deg,#a9bccd 0%,#c9d5df 35%,#dde2e6 70%,#d2cbc2 86%,#bcae9f 100%)}
.headline{position:absolute;left:284px;top:204px;color:#fff;font-weight:400;text-shadow:1px 2px 3px rgba(0,0,0,.25);line-height:1}
.headline em{display:block;font-style:italic;font-size:48px}
.headline span{display:block;font-size:53px;margin-top:6px}

.btn{position:absolute;display:flex;align-items:center;border-radius:8px;color:#fff;font-size:23px;
  border:2px solid #fff;box-shadow:0 2px 5px rgba(0,0,0,.35);padding-left:18px;text-decoration:none;overflow:hidden}
.btn::after{content:"";position:absolute;right:0;top:0;bottom:0;width:26px;background:rgba(0,0,0,.12);border-left:1px solid rgba(255,255,255,.35)}
.btn svg{position:absolute;right:8px;top:50%;margin-top:-6px;z-index:1}
.btn-demo{background:linear-gradient(180deg,var(--teal-light),var(--teal))}
.btn-more{background:linear-gradient(180deg,var(--orange-light),var(--orange));left:637px;top:329px;width:213px;height:50px;padding-left:34px}

.dots{position:absolute;left:931px;top:465px;display:flex;gap:5px}
.dots i{width:13px;height:13px;border-radius:50%;background:#111;border:2px solid #fff}
.dots i.on{background:var(--orange)}

.nav{position:absolute;left:145px;top:9px;width:912px;height:36px;display:flex;border-radius:6px;overflow:hidden;
  background:linear-gradient(180deg,var(--nav-top),var(--nav-bottom));border:1px solid #c9c9c9}
.nav a{display:flex;align-items:center;justify-content:center;color:#fff;font-weight:700;font-size:12.5px;letter-spacing:.6px;
  text-decoration:none;text-shadow:0 1px 1px rgba(0,0,0,.45);border-right:1px solid #9c9c9c;box-shadow:inset -1px 0 #eee}
.nav .spacer{flex:1}

.header{position:absolute;left:145px;top:56px;width:912px;height:78px;background:#fff;border-radius:6px;box-shadow:0 10px 10px -6px rgba(0,0,0,.45)}
.brand{position:absolute;left:16px;top:12px;display:flex;align-items:center;gap:10px}
.brand i{width:44px;height:44px;border-radius:50%;background:var(--teal)}
.brand b{font-weight:400;font-size:44px;color:var(--teal);line-height:1}
.header .btn-demo{left:683px;top:12px;width:211px;height:49px}

.panel{position:absolute;left:145px;top:493px;width:912px;height:343px;background:var(--panel);border-radius:8px;box-shadow:0 2px 6px rgba(0,0,0,.3)}
.col-title{position:absolute;top:24px;font-size:19px;color:var(--heading);font-weight:400}
.card{position:absolute;top:58px;width:231px;height:254px;border:1px solid #ddd;border-radius:4px;box-shadow:0 1px 3px rgba(0,0,0,.15);background:#fff}
.card-media{position:absolute;left:5px;top:5px;width:221px;height:92px;border-radius:3px;background:#777}
.card h3{position:absolute;left:12px;top:114px;font-size:11.5px;font-weight:700;color:var(--link-blue)}
.card p{position:absolute;left:12px;top:137px;width:212px;font-size:11.3px;line-height:13.6px;color:#555}
.card .more{position:absolute;right:22px;top:226px;font-size:10.5px;font-weight:700;color:var(--heading);text-decoration:none}
.card .author{position:absolute;left:88px;top:216px;font-size:10.5px;font-weight:700;color:var(--heading);line-height:12px}
.arrow-btn{position:absolute;top:157px;width:34px;height:34px;border-radius:50%;background:linear-gradient(180deg,#fff,#d6d6d6);box-shadow:0 1px 3px rgba(0,0,0,.35);display:flex;align-items:center;justify-content:center}

.footer{position:absolute;left:0;top:865px;width:1200px;height:73px;background:var(--footer);color:#fff;font-size:10.5px}
.footer .links{position:absolute;left:145px;top:15px}
.footer .copy{position:absolute;left:145px;top:48px}
.follow{position:absolute;left:512px;top:23px;display:flex;align-items:center;gap:10px}
.follow i{width:30px;height:30px;border-radius:4px;background:#3a6ea8;box-shadow:0 1px 2px rgba(0,0,0,.4)}
.follow i:nth-of-type(2){background:#1a7bb0}
.follow i:nth-of-type(3){background:#7fd3ea}
.footer .btn-demo{left:854px;top:12px;width:214px;height:50px}
</style>
</head>
<body>
<div class="page">
  <section class="hero">
    <div class="hero-scene" role="img" aria-label="Sky and desert horizon scene with currency gears on the left and a red growth arrow on the right, each with a businessman figure"></div>
    <h1 class="headline"><em>We empower</em><span>investment management</span></h1>
    <a class="btn btn-more" href="#">Know more<svg width="8" height="12" viewBox="0 0 8 12"><path d="M0 0L8 6L0 12Z" fill="#fff"/></svg></a>
    <div class="dots"><i class="on"></i><i></i><i></i><i></i></div>
  </section>

  <nav class="nav">
    <a href="#" style="width:92px" aria-label="Home"><svg width="20" height="17" viewBox="0 0 20 17"><path d="M10 0L0 8h3v9h5v-6h4v6h5V8h3z" fill="#555"/></svg></a>
    <a href="#" style="width:133px">Company</a>
    <a href="#" style="width:136px">Solutions</a>
    <a href="#" style="width:131px">Careers</a>
    <a href="#" style="width:167px">Whitepapers</a>
    <a href="#" style="width:141px">Contacts</a>
    <span class="spacer"></span>
  </nav>

  <header class="header">
    <div class="brand"><i></i><b>fundora</b></div>
    <a class="btn btn-demo" href="#">Request Demo<svg width="8" height="12" viewBox="0 0 8 12"><path d="M0 0L8 6L0 12Z" fill="#fff"/></svg></a>
  </header>

  <main class="panel">
    <a class="arrow-btn" href="#" style="left:12px" aria-label="Previous"><svg width="10" height="14" viewBox="0 0 10 14"><path d="M8 1L2 7l6 6" stroke="#222" stroke-width="3" fill="none"/></svg></a>
    <a class="arrow-btn" href="#" style="left:866px" aria-label="Next"><svg width="10" height="14" viewBox="0 0 10 14"><path d="M2 1l6 6-6 6" stroke="#222" stroke-width="3" fill="none"/></svg></a>

    <h2 class="col-title" style="left:66px">Recent White Papers</h2>
    <article class="card" style="left:67px">
      <div class="card-media" style="background:linear-gradient(180deg,#9a9a9a,#b5b5b5)" role="img" aria-label="Stack of white paper sheets"></div>
      <h3>The SHARPE-Less-ness...</h3>
      <p>The paper explains how the risk adjusted performance ratios can be grossly misleading in certain market scenarios. Certain remedials are also discussed.</p>
      <a class="more" href="#">Read / Download...</a>
    </article>

    <h2 class="col-title" style="left:338px">Testimonials</h2>
    <article class="card" style="left:339px">
      <div class="card-media">
        <svg width="221" height="92" viewBox="0 0 221 92">
          <text x="20" y="52" font-family="Georgia,serif" font-size="56" fill="#999">“</text>
          <text x="194" y="92" font-family="Georgia,serif" font-size="56" fill="#999">”</text>
          <g stroke="#999" stroke-width="1" stroke-dasharray="1 1">
            <line x1="54" y1="37" x2="160" y2="37"/><line x1="54" y1="48" x2="175" y2="48"/><line x1="54" y1="59" x2="125" y2="59"/>
          </g>
        </svg>
      </div>
      <h3>Endorsed by the best</h3>
      <p>"We proudly present our attribution analysis to our clients.<br>I am sure Fundora's solutions will become a must have for all investment management functions."</p>
      <div class="author">Mr. Arjun Mehta<br>(ex - Northbay Capital AMC)</div>
    </article>

    <h2 class="col-title" style="left:610px">Media</h2>
    <article class="card" style="left:611px">
      <div class="card-media">
        <svg width="221" height="92" viewBox="0 0 221 92">
          <circle cx="113" cy="45" r="24" fill="none" stroke="#ccc" stroke-width="7"/>
          <path d="M108 36l12 9-12 9z" fill="#ddd"/>
        </svg>
      </div>
      <h3>Lorem ipsum Media</h3>
      <p>The paper explains how the risk adjusted performance ratios can be grossly misleading in certain market scenarios. Certain remedials are also discussed.</p>
      <a class="more" href="#">Download Video / Media...</a>
    </article>
  </main>

  <footer class="footer">
    <div class="links">Company : Solutions : Whitepapers : Careers : Contacts</div>
    <div class="copy">Copyright © fundora.com. All rights reserved.</div>
    <div class="follow"><span>Follow us on:</span><i></i><i></i><i></i></div>
    <a class="btn btn-demo" href="#">Request Demo<svg width="8" height="12" viewBox="0 0 8 12"><path d="M0 0L8 6L0 12Z" fill="#fff"/></svg></a>
  </footer>
</div>
</body>
</html>
```